DRU online New Year's greeting card**

We would like to send an original digital New year's card via Email to all our customers. We are a company located in Belgium (Europe). We load and unload new cars from Roll-on-Roll-off vessels. More info can be found on our website: www.druterminals-example.com

```html
<!DOCTYPE html>
<html lang="en">
<head>
<meta charset="utf-8">
<title>DRU – Happy New Year 2021</title>
<link href="https://fonts.googleapis.com/css2?family=Open+Sans:wght@300;400;700&display=swap" rel="stylesheet">
<style>
  :root {
    --sky-top: #ffffff;
    --sky-mid: #c9ecfb;
    --sky-bottom: #6ccbf3;
    --navy: #1c4f8f;
    --blue: #2f6db5;
    --steel: #5a8bd0;
    --light: #62c0ee;
    --white: #ffffff;
    --string: #2a5f9e;
  }
  * { margin: 0; padding: 0; box-sizing: border-box; }
  html, body { width: 1200px; height: 900px; overflow: hidden; }
  body { font-family: "Open Sans", Arial, sans-serif; }
  .card {
    position: relative;
    width: 1200px;
    height: 900px;
    overflow: hidden;
    background: linear-gradient(to bottom, var(--sky-top) 0%, var(--sky-mid) 30%, var(--sky-bottom) 100%);
  }
  .decor { position: absolute; inset: 0; }
  .greeting {
    position: absolute;
    top: 500px;
    left: 0;
    width: 100%;
    text-align: center;
    font-size: 34px;
    font-weight: 400;
    letter-spacing: 9px;
    color: var(--navy);
  }
  .year {
    position: absolute;
    top: 545px;
    left: 0;
    width: 100%;
    text-align: center;
    font-size: 222px;
    font-weight: 300;
    line-height: 1;
    letter-spacing: 4px;
    color: var(--white);
  }
  .brand {
    position: absolute;
    left: 1000px;
    top: 770px;
    width: 180px;
    height: 90px;
    background: var(--white);
    display: flex;
    align-items: center;
    justify-content: center;
    gap: 12px;
  }
  .brand-dot {
    width: 22px;
    height: 22px;
    border-radius: 50%;
    background: var(--navy);
  }
  .brand-name {
    font-size: 44px;
    font-weight: 700;
    color: var(--navy);
  }
  .website {
    position: absolute;
    right: 20px;
    top: 864px;
    font-size: 15px;
    color: var(--navy);
  }
</style>
</head>
<body>
<main class="card">
  <svg class="decor" width="1200" height="900" viewBox="0 0 1200 900">
    <defs>
      <polygon id="hex" points="0,-1 0.866,-0.5 0.866,0.5 0,1 -0.866,0.5 -0.866,-0.5"/>
    </defs>

    <g class="snow" fill="#ffffff" opacity="0.85">
      <circle cx="80" cy="120" r="3"/><circle cx="210" cy="300" r="2"/>
      <circle cx="330" cy="380" r="3"/><circle cx="420" cy="330" r="2"/>
      <circle cx="560" cy="400" r="3"/><circle cx="640" cy="320" r="2"/>
      <circle cx="780" cy="420" r="3"/><circle cx="860" cy="350" r="2"/>
      <circle cx="960" cy="470" r="3"/><circle cx="1040" cy="260" r="2"/>
      <circle cx="1150" cy="520" r="3"/><circle cx="60" cy="560" r="2"/>
      <circle cx="140" cy="640" r="3"/><circle cx="260" cy="720" r="2"/>
      <circle cx="110" cy="820" r="3"/><circle cx="330" cy="860" r="2"/>
      <circle cx="290" cy="600" r="2"/><circle cx="900" cy="640" r="3"/>
      <circle cx="980" cy="700" r="2"/><circle cx="880" cy="820" r="3"/>
      <circle cx="1120" cy="640" r="2"/><circle cx="720" cy="480" r="2"/>
      <circle cx="480" cy="470" r="3"/><circle cx="200" cy="480" r="2"/>
      <circle cx="1060" cy="150" r="2"/><circle cx="600" cy="90" r="2"/>
    </g>
    <g class="bubbles" fill="none" stroke="#a9d7ee" stroke-width="2">
      <circle cx="70" cy="80" r="6"/><circle cx="560" cy="40" r="5"/>
      <circle cx="360" cy="60" r="4"/><circle cx="1150" cy="90" r="6"/>
      <circle cx="810" cy="110" r="5"/><circle cx="30" cy="230" r="4"/>
    </g>

    <g class="strings" stroke="var(--string)" stroke-width="2">
      <line x1="128" y1="0" x2="128" y2="340"/>
      <line x1="260" y1="0" x2="260" y2="88" stroke-dasharray="3 7"/>
      <line x1="466" y1="0" x2="466" y2="144"/>
      <line x1="690" y1="0" x2="690" y2="148"/>
      <line x1="910" y1="0" x2="910" y2="78" stroke-dasharray="3 7"/>
      <line x1="1100" y1="0" x2="1100" y2="310"/>
    </g>

    <g class="ornaments" stroke-linejoin="round" stroke-width="0.12">
      <use href="#hex" transform="translate(128 430) scale(90)" fill="var(--blue)" stroke="var(--blue)" role="img" aria-label="Ornament with a car carrier ship icon"/>
      <use href="#hex" transform="translate(260 160) scale(72)" fill="var(--navy)" stroke="var(--navy)" role="img" aria-label="Ornament with a car loading ramp icon"/>
      <use href="#hex" transform="translate(466 216) scale(72)" fill="var(--light)" stroke="var(--light)" role="img" aria-label="Ornament with a car and circular arrows icon"/>
      <use href="#hex" transform="translate(690 220) scale(72)" fill="var(--navy)" stroke="var(--navy)" role="img" aria-label="Ornament with a crane loading a ship icon"/>
      <use href="#hex" transform="translate(910 156) scale(78)" fill="var(--steel)" stroke="var(--steel)" role="img" aria-label="Ornament with wind turbines icon"/>
      <use href="#hex" transform="translate(1100 390) scale(80)" fill="var(--navy)" stroke="var(--navy)" role="img" aria-label="Ornament with an electric car icon"/>
    </g>
  </svg>

  <p class="greeting">HAPPY NEW YEAR</p>
  <p class="year">2021</p>

  <div class="brand">
    <span class="brand-dot"></span>
    <span class="brand-name">DRU</span>
  </div>
  <p class="website">www.druterminals-example.com</p>
</main>
</body>
</html>
```